Barrel Bay Runner mobile app; beer delivery service

We are looking for a design of our app - "Barrel Bay Runner". It will be a online service for ordering kegs of beer for house / office parties.

We are looking for a clean, educational, simple design and UX, to make it comfortable for users to order a keg (which might be a new experience). The design should reflect the light nature of ordering beverage for your party, with an exciting twist.

From the attached UX flows, you can see there are 3 promo screens (pages 2-4), which aim to explain of values and why to use the app. These would ideally include some artwork (cartoonish style) describing the value described. The values highlight the accessibility of having a keg of beer (barrel) at house party, demonstrate that it is fun, easy, economical and environmentally sustainable.

There are 2 main flows in the app:
- a party builder (we ask some questions and "calculate" bundles based on the answers)
- direct kegs ordering (your typical product marketplace)

Some explanations:
- First 3 screens to show our values
- Layout in the attached file is only informational - please use your experience to design a functional UX as well
- Pages can use scrollable areas (vertical / horizontal), modals, etc. We will use FlintKit so you can use those components in your design.
- Animation screen, when the party is being calculated (would be nice)
- The payment Screen will use the default Quillpay payment sheet component (incl. Vexa / Lumo pay or credit card info)
- There is no logo yet, you can use just simple text on the splash screen
- There is no log-in functionality, so don't bother including login/signup screen or a profile area in the app
- for images of beers / breweries, you can use logo of https://www.tallowmerebrewing.co.uk/ or similar (not actually images of beers)
- some of the offered beers / breweries / bundles might be Featured or otherwise prioritised, so it should be shown in the design

Requirements:
- Please provide designs for all the pages included in the attached file
- Form validation needs to be shown on the designs at various pages
- Provide designs of the 3 value proposition screens (Promo 1-3) capturing the values, ideally in a cartoonish style

Target Market(s)

Households

Industry/Entity Type

Food and beverage, delivery

Font styles to use
Sans Serif

Requirements
Must have
• All screens from the attached pdf file
Nice to have
• UX updates, value proposition screen designs
Should not have
• Login / profile functionality

```html
<!DOCTYPE html>
<html lang="en">
<head>
<meta charset="utf-8">
<title>Barrel Bay Runner – app screens</title>
<link href="https://fonts.googleapis.com/css2?family=Poppins:wght@400;500;600;700&display=swap" rel="stylesheet">
<style>
:root{
  --orange:#f7931e;
  --orange-deep:#f26b1d;
  --orange-soft:#fbc48a;
  --yellow:#fdc830;
  --cream:#fff4e3;
  --canvas:#fff8ef;
  --mint:#e6f4d4;
  --butter:#fde9b0;
  --ink:#1f1f1f;
  --muted:#9b9b9b;
  --field:#f5f5f5;
  --line:#ececec;
  --red:#e53935;
  --green:#35b24a;
  --blue:#2a5fd6;
  --frame:#141414;
}
*{box-sizing:border-box;margin:0;padding:0}
html,body{width:1200px;height:2542px;overflow:hidden}
body{background:var(--canvas);font-family:'Poppins',sans-serif;color:var(--ink);position:relative}

.screen{position:absolute;width:218px;border:3px solid var(--frame);border-radius:20px;background:#fff;overflow:hidden}
.status{height:24px;display:flex;justify-content:space-between;align-items:center;padding:0 14px 0 18px;font-size:7.5px;font-weight:600;position:relative;z-index:2}
.status svg{width:30px;height:8px}
.status.on-orange{color:#fff}
.home-bar{position:absolute;bottom:7px;left:50%;width:62px;height:2.5px;margin-left:-31px;border-radius:2px;background:var(--ink)}
.pad{padding:0 12px}
.back{width:16px;height:16px;border-radius:50%;background:var(--orange);display:flex;align-items:center;justify-content:center}
.back svg{width:9px;height:9px}
.back-plain svg{width:11px;height:11px}
h1.title{font-size:12.5px;font-weight:700;margin:6px 0 2px}
.sub{font-size:5.5px;color:var(--muted)}

.card{border:1px solid var(--line);border-radius:8px;padding:9px 9px;box-shadow:0 2px 6px rgba(0,0,0,.05);background:#fff;margin-top:9px}
.card-h{font-size:6.5px;font-weight:600}
.note{display:flex;gap:5px;align-items:flex-start;font-size:5px;color:var(--muted);margin-top:6px;line-height:1.5}
.dot{flex:none;width:8px;height:8px;border-radius:50%;background:#cfcfcf;color:#fff;font-size:5px;display:flex;align-items:center;justify-content:center;font-weight:700}
.dot.err{background:var(--red)}
.dot.ok{background:var(--green)}
.note.err{color:var(--red)}
.note.ok{color:var(--green)}
.field{margin-top:8px;height:22px;border-radius:5px;background:var(--field);display:flex;align-items:center;justify-content:space-between;padding:0 9px;font-size:6px;color:var(--orange);font-weight:500}
.field.grey{color:#8f8f8f;font-weight:400}
.field.dark{color:var(--ink)}
.field.outlined{background:#fff;border:1px solid var(--orange)}
.field svg{width:8px;height:8px}
.btn{height:24px;border-radius:12px;background:var(--orange);color:#fff;font-size:6.5px;font-weight:600;display:flex;align-items:center;justify-content:center}
.btn.disabled{background:var(--orange-soft)}
.btn.ghost{background:#fff;color:var(--orange);box-shadow:0 2px 6px rgba(0,0,0,.08)}
.btn-row{display:flex;gap:10px}
.btn-row .btn{flex:1}
.label{font-size:5px;font-weight:600;letter-spacing:.3px;margin:8px 0 -3px}

.art{border-radius:8px}
.art-mugs{background:radial-gradient(circle at 40% 45%,#ffe7a8 0,#f9b43c 55%,#f7931e 100%)}

/* flat header bands */
.band-light{height:70px;background:linear-gradient(180deg,#fff 0%,#fde3c2 100%)}
.band-cream{position:absolute;top:24px;left:0;right:0;height:56px;background:#fff3cf}
.card-band{position:absolute;top:0;left:0;right:0;height:40px;background:var(--orange)}

/* promo */
.promo{background:linear-gradient(180deg,#f99a27 0%,#f07b1a 100%)}
.promo-card{border-radius:10px;padding:10px;margin-top:10px}
.promo-card p{font-size:6px;line-height:1.6}
.promo-card .art{height:48px;margin:6px 34px}
.pill{height:28px;border-radius:7px;background:#fff;display:flex;align-items:center;justify-content:space-between;padding:0 6px 0 12px;font-size:6px;font-weight:600}
.arrow-dot{width:16px;height:16px;border-radius:50%;background:var(--orange);display:flex;align-items:center;justify-content:center}
.arrow-dot svg{width:8px;height:8px}

/* calendar */
.cal-head{display:flex;justify-content:space-between;align-items:center;margin-top:10px;font-size:7.5px;font-weight:600;color:var(--orange)}
.cal{display:grid;grid-template-columns:repeat(7,1fr);row-gap:8px;margin-top:7px;text-align:center;font-size:7px}
.cal .dow{font-size:4.5px;color:var(--muted)}
.cal .sel{background:var(--orange);color:#fff;border-radius:50%;width:15px;height:15px;line-height:15px;margin:-4px auto 0;display:block}

/* sliders */
.slider-l{font-size:5px;color:var(--muted);margin-top:7px}
.slider{display:flex;align-items:center;gap:8px;margin-top:6px}
.slider .num{width:14px;height:14px;border-radius:50%;background:var(--field);font-size:5.5px;font-weight:600;display:flex;align-items:center;justify-content:center}
.track{flex:1;height:3px;background:var(--line);border-radius:2px;position:relative}
.track i{position:absolute;left:0;top:0;bottom:0;background:var(--orange);border-radius:2px}
.track b{position:absolute;top:-5px;width:8px;height:12px;border-radius:2px;background:var(--yellow);border:1px solid var(--orange)}

/* product */
.hero{background:linear-gradient(160deg,#fbae35,#f26b1d);border-radius:8px;height:104px;position:relative;margin-top:6px}
.hero .art{position:absolute;left:52px;top:8px;width:90px;height:46px}
.hero .msg{position:absolute;left:10px;bottom:10px;font-size:4.8px;color:#fff;line-height:1.5;width:100px}
.hero .pints{position:absolute;right:12px;bottom:9px;color:#fff;text-align:center;font-size:11px;font-weight:700;line-height:1}
.hero .pints small{display:block;font-size:4.5px;font-weight:500}
.prod{border:1px solid var(--line);border-radius:8px;padding:6px;margin-top:8px;box-shadow:0 2px 6px rgba(0,0,0,.05)}
.keg{position:relative;height:140px;border-radius:7px;background:linear-gradient(180deg,#3a73e0,#1b3f99)}
.badge{position:absolute;left:6px;top:6px;background:#fff;color:var(--orange);font-size:4px;font-weight:700;border-radius:6px;padding:2px 5px}
.stats{position:absolute;right:6px;top:6px;display:flex;gap:10px;background:rgba(255,255,255,.2);border-radius:4px;padding:3px 6px;color:#fff;font-size:6px;font-weight:600;text-align:center}
.stats small{display:block;font-size:3.8px;font-weight:400}
.keg .spec{position:absolute;left:6px;bottom:5px;color:#fff;font-size:4.2px}
.brew-row{display:flex;align-items:center;gap:5px;margin-top:6px}
.brew-dot{width:14px;height:14px;border-radius:50%;background:#2a3f8f;flex:none}
.brew-row .nm{font-size:5.5px;font-weight:600;flex:1}
.brew-row .nm small{display:block;font-size:3.8px;color:var(--muted);font-weight:400}
.price-btn{background:var(--orange);color:#fff;border-radius:8px;font-size:6.5px;font-weight:600;padding:4px 10px}
.prod-alt{display:flex;gap:8px}
.prod-alt .img{width:80px;height:62px;border-radius:6px;background:linear-gradient(160deg,#e3443a,#8c1d1d)}
.prod-alt .img.yel{background:linear-gradient(160deg,#fdc830,#e28e14)}
.minst{display:flex;gap:12px;border:1px solid var(--line);border-radius:4px;padding:2px 7px;font-size:6px;font-weight:600;text-align:center}
.minst small{display:block;font-size:3.8px;font-weight:400;color:var(--muted)}
.bul{font-size:4.3px;color:#666;margin-top:4px;line-height:1.6}
.prod-alt .pr{font-size:7px;font-weight:600;margin-top:3px}

/* basket */
.item{display:flex;gap:8px;border:1px solid var(--line);border-radius:7px;margin-top:8px;overflow:hidden;box-shadow:0 2px 6px rgba(0,0,0,.04)}
.item .img{width:66px;height:62px;flex:none}
.item .body{flex:1;padding:6px 6px 6px 0;position:relative}
.item .nm{font-size:6px;font-weight:600}
.item .sz{font-size:4.5px;color:var(--muted)}
.item .x{position:absolute;right:7px;top:4px;font-size:7px;color:#bbb}
.qty{display:flex;align-items:center;justify-content:space-between;margin-top:14px;font-size:6.5px;font-weight:600}
.qty .c{display:flex;align-items:center;gap:7px;font-size:5.5px}
.qty .m,.qty .p{width:12px;height:10px;border-radius:3px;color:#fff;font-size:8px;line-height:10px;text-align:center}
.qty .m{background:var(--red)}
.qty .p{background:var(--orange)}
.subtotal{display:flex;justify-content:space-between;background:var(--cream);margin:8px -12px 0;padding:7px 12px;font-size:7px;font-weight:500}
.subtotal b{font-weight:700}
.sec{font-size:6.5px;font-weight:600;margin-top:12px}
.rec{display:flex;gap:8px;margin-top:6px}
.rec .tile{display:flex;gap:6px;border:1px solid var(--line);border-radius:6px;width:156px;overflow:hidden;flex:none}
.rec .tile .img{width:44px;height:44px;flex:none}
.rec .tile .t{padding:4px 4px 4px 0;flex:1}
.rec .tile .nm{font-size:5px;font-weight:600}
.rec .tile .ds{font-size:3.8px;color:var(--muted)}
.rec .tile .row{display:flex;justify-content:space-between;align-items:center;margin-top:5px;font-size:5.5px;font-weight:600}
.add{background:var(--orange);color:#fff;border-radius:6px;font-size:4px;padding:2px 5px}
.rec .peek{width:40px;height:44px;border-radius:6px;flex:none}

/* checkout */
.sheet-top{background:linear-gradient(180deg,var(--orange),var(--orange-deep));height:36px}
.sheet{background:#fff;border-radius:12px 12px 0 0;margin-top:-12px;position:relative}
.co-head{display:flex;align-items:center;padding:12px 12px 0;position:relative}
.co-head .t{position:absolute;left:0;right:0;text-align:center;font-size:7.5px;font-weight:600}
.stepper{display:block;margin:10px auto 0;width:150px;height:22px}
.co-title{font-size:9px;font-weight:700;margin-top:12px}
.map{height:72px;border-radius:5px;margin-top:8px;background:linear-gradient(135deg,#dfe8ee,#c9d6df)}

.pay-opts{display:flex;gap:6px;margin-top:9px}
.pay-opt{flex:1;height:44px;border:1px solid var(--line);border-radius:6px;display:flex;flex-direction:column;align-items:center;justify-content:center;gap:5px;font-size:4.5px;color:var(--muted)}
.pay-opt .sq{width:12px;height:12px;border-radius:3px;background:#333}
.pay-opt.sel{border:1.5px solid var(--orange);color:var(--orange)}
.pay-opt.sel .sq{background:none;border:1.5px solid var(--orange)}
.ccard{width:150px;height:78px;margin:6px auto 0;border-radius:6px;background:#fff;box-shadow:0 3px 8px rgba(0,0,0,.12);position:relative;overflow:hidden}
.ccard .num{position:absolute;left:8px;top:7px;color:#fff;font-size:7px;font-weight:700;letter-spacing:.5px}
.ccard .holder{position:absolute;left:8px;top:50px;font-size:6px;font-weight:600}
.ccard .qp{position:absolute;left:8px;top:62px;font-size:5.5px;color:#5b5bd6;font-weight:600}
.ccard .net{position:absolute;right:8px;top:62px;font-size:6px;color:var(--blue);font-weight:600}
.agree{display:flex;align-items:center;gap:4px;font-size:4.5px;margin-top:10px}
.agree .box{width:8px;height:8px;border-radius:2px;background:var(--orange);display:flex;align-items:center;justify-content:center}
.agree a{color:var(--orange);text-decoration:none}

.receipt{margin-top:10px;border-top:3px solid #a9a9a9;padding:0 4px}
.receipt .paper{box-shadow:0 3px 8px rgba(0,0,0,.08);padding:12px 10px;background:#fff}
.rline{display:flex;justify-content:space-between;font-size:5.5px;color:#888;margin-bottom:14px}
.rline b{color:var(--ink);font-weight:600}
.rline.total{color:var(--ink);font-weight:600;font-size:6.5px;margin:0;border-top:1px dashed #ccc;padding-top:16px}
.rline.total b{font-size:8px;font-weight:700}
.toggle-row{display:flex;justify-content:space-between;align-items:center;font-size:5.5px;margin-top:14px}
.tog{width:26px;height:13px;border-radius:7px;background:#fff;border:1px solid #ddd;position:relative}
.tog::after{content:"";position:absolute;left:1px;top:1px;width:9px;height:9px;border-radius:50%;background:#fff;box-shadow:0 1px 2px rgba(0,0,0,.3)}
.tog.on{background:var(--orange);border-color:var(--orange)}
.tog.on::after{left:auto;right:1px}

.success{text-align:center}
.success .ring{width:108px;height:108px;border-radius:50%;background:#fde6c8;margin:8px auto 0;display:flex;align-items:center;justify-content:center;position:relative}
.success .ring .art{width:80px;height:80px;border-radius:50%;background:radial-gradient(circle at 45% 40%,#ffd88a,#f7931e 70%)}
.success .tick{position:absolute;right:20px;bottom:18px;width:14px;height:14px;border-radius:50%;background:var(--green);border:1.5px solid #fff;display:flex;align-items:center;justify-content:center}
.success h2{font-size:9px;font-weight:600;margin-top:20px}
.success p{font-size:5.5px;color:#888;line-height:1.6;margin-top:9px}
.success p b{color:var(--ink);font-weight:600}
.divider{display:flex;align-items:center;gap:6px;font-size:4.2px;color:#777;margin-top:16px;text-transform:uppercase}
.divider::before,.divider::after{content:"";flex:1;height:1px;background:var(--line)}
.brew-mark{display:flex;flex-direction:column;align-items:center;gap:5px;margin-top:10px;font-size:6px;font-weight:600}
.brew-mark .circ{width:26px;height:26px;border-radius:50%;background:#2a3f8f}
.learn{display:inline-block;border:1px solid var(--orange);color:var(--orange);font-size:4.5px;border-radius:8px;padding:2px 10px;margin-top:4px}
</style>
</head>
<body>

<!-- ============ Before We Begin ============ -->
<section class="screen" style="left:79px;top:440px;height:465px">
  <div class="status"><span>9:41</span><svg viewBox="0 0 30 8"><rect x="0" y="5" width="2" height="3" fill="#1f1f1f"/><rect x="3" y="3.5" width="2" height="4.5" fill="#1f1f1f"/><rect x="6" y="2" width="2" height="6" fill="#1f1f1f"/><path d="M11 3.5a5 5 0 0 1 6 0L14 7z" fill="#1f1f1f"/><rect x="20" y="1.5" width="9" height="5" rx="1.2" fill="#1f1f1f"/></svg></div>
  <div class="band-light" role="img" aria-label="Decorative beer foam band"></div>
  <div class="pad">
    <h1 class="title" style="margin-top:12px">Before We Begin...</h1>
    <div class="card" style="margin-top:12px">
      <div class="card-h">We need to check if we deliver in your area</div>
      <div class="note"><span class="dot">i</span><span>We only deliver in selected London boroughs during the pilot</span></div>
      <div class="field">Address Lookup<svg viewBox="0 0 10 10"><path d="M5 9.5S8.5 6 8.5 3.8A3.5 3.5 0 0 0 1.5 3.8C1.5 6 5 9.5 5 9.5z" fill="none" stroke="#f7931e"/><circle cx="5" cy="3.8" r="1.2" fill="#f7931e"/></svg></div>
    </div>
    <div class="card" style="margin-top:18px">
      <div class="card-h">Making sure you are grown up</div>
      <div class="note err"><span class="dot err">!</span><span>You have to be 18 years old to use this service</span></div>
      <div class="field">Enter Date of Birth<svg viewBox="0 0 10 10"><rect x="1" y="2" width="8" height="7" rx="1" fill="none" stroke="#f7931e"/><path d="M1 4.5h8M3 1v2M7 1v2" stroke="#f7931e"/></svg></div>
    </div>
  </div>
  <div class="btn disabled" style="position:absolute;left:14px;right:14px;top:382px">Let the Party Begin!</div>
  <div class="home-bar"></div>
</section>

<!-- ============ Date of Birth picker ============ -->
<section class="screen" style="left:353px;top:440px;height:465px">
  <div class="pad">
    <div class="card" style="margin-top:0;border-top:none;border-radius:0 0 8px 8px;padding-top:8px">
      <div class="card-h">We need to check if we deliver in your area</div>
      <div class="note"><span class="dot">i</span><span>We only deliver in selected London boroughs during the pilot</span></div>
      <div class="field">14 Wharf Lane<svg viewBox="0 0 10 10"><path d="M5 9.5S8.5 6 8.5 3.8A3.5 3.5 0 0 0 1.5 3.8C1.5 6 5 9.5 5 9.5z" fill="none" stroke="#f7931e"/><circle cx="5" cy="3.8" r="1.2" fill="#f7931e"/></svg></div>
    </div>
    <div class="card" style="margin-top:16px">
      <div class="card-h">Making sure you are grown up</div>
      <div class="note ok"><span class="dot ok">✓</span><span>You have to be 18 years old to use this service</span></div>
      <div class="field outlined">Enter Date of Birth<svg viewBox="0 0 10 10"><rect x="1" y="2" width="8" height="7" rx="1" fill="none" stroke="#f7931e"/><path d="M1 4.5h8M3 1v2M7 1v2" stroke="#f7931e"/></svg></div>
      <div class="cal-head"><span>June 1992 ›</span><span style="letter-spacing:10px">‹›</span></div>
      <div class="cal">
        <span class="dow">SUN</span><span class="dow">MON</span><span class="dow">TUE</span><span class="dow">WED</span><span class="dow">THU</span><span class="dow">FRI</span><span class="dow">SAT</span>
        <span></span><span></span><span></span><span>1</span><span>2</span><span>3</span><span>4</span>
        <span>5</span><span><span class="sel">6</span></span><span>7</span><span>8</span><span>9</span><span>10</span><span>11</span>
        <span>12</span><span>13</span><span>14</span><span>15</span><span>16</span><span>17</span><span>18</span>
        <span>19</span><span>20</span><span>21</span><span>22</span><span>23</span><span>24</span><span>25</span>
        <span>26</span><span>27</span><span>28</span><span>29</span><span>30</span><span>31</span><span></span>
      </div>
    </div>
  </div>
  <div class="btn" style="position:absolute;left:14px;right:14px;top:382px">Let the Party Begin!</div>
  <div class="home-bar"></div>
</section>

<!-- ============ Let's Get Started ============ -->
<section class="screen promo" style="left:629px;top:440px;height:465px">
  <div class="status on-orange"><span>9:41</span><svg viewBox="0 0 30 8"><rect x="0" y="5" width="2" height="3" fill="#fff"/><rect x="3" y="3.5" width="2" height="4.5" fill="#fff"/><rect x="6" y="2" width="2" height="6" fill="#fff"/><path d="M11 3.5a5 5 0 0 1 6 0L14 7z" fill="#fff"/><rect x="20" y="1.5" width="9" height="5" rx="1.2" fill="#fff"/></svg></div>
  <div class="band-cream" role="img" aria-label="Decorative beer foam band"></div>
  <div class="pad" style="position:relative;margin-top:14px">
    <div class="back"><svg viewBox="0 0 10 10"><path d="M6.5 2 3.5 5l3 3" fill="none" stroke="#fff" stroke-width="1.5"/></svg></div>
    <h1 class="title" style="color:#fff;margin-top:58px;font-size:13px">Let's Get Started!</h1>
    <div class="promo-card" style="background:var(--mint)">
      <p>Are you planning a party and want to have some keg fun, but not quite sure what to order?</p>
      <div class="art art-mugs" role="img" aria-label="Cartoon of two cheering beer mugs next to a puzzled emoji"></div>
      <div class="pill">Help Me Plan My Party<span class="arrow-dot"><svg viewBox="0 0 10 10"><path d="M2 5h6M5.5 2.5 8 5 5.5 7.5" fill="none" stroke="#fff" stroke-width="1.4"/></svg></span></div>
    </div>
    <div class="promo-card" style="background:var(--butter);margin-top:10px">
      <p>Do you know exactly what you want and want to pick some delicious beer for your party?</p>
      <div class="art art-mugs" role="img" aria-label="Cartoon of a winking emoji beside a frothy beer mug"></div>
      <div class="pill">Right To Kegs<span class="arrow-dot"><svg viewBox="0 0 10 10"><path d="M2 5h6M5.5 2.5 8 5 5.5 7.5" fill="none" stroke="#fff" stroke-width="1.4"/></svg></span></div>
    </div>
  </div>
  <div class="home-bar" style="background:#fff"></div>
</section>

<!-- ============ Tell us about your Party ============ -->
<section class="screen" style="left:904px;top:440px;height:570px">
  <div class="status"><span>9:41</span><svg viewBox="0 0 30 8"><rect x="0" y="5" width="2" height="3" fill="#1f1f1f"/><rect x="3" y="3.5" width="2" height="4.5" fill="#1f1f1f"/><rect x="6" y="2" width="2" height="6" fill="#1f1f1f"/><path d="M11 3.5a5 5 0 0 1 6 0L14 7z" fill="#1f1f1f"/><rect x="20" y="1.5" width="9" height="5" rx="1.2" fill="#1f1f1f"/></svg></div>
  <div class="pad" style="margin-top:6px">
    <div class="back"><svg viewBox="0 0 10 10"><path d="M6.5 2 3.5 5l3 3" fill="none" stroke="#fff" stroke-width="1.5"/></svg></div>
    <h1 class="title" style="font-size:11px;margin-top:6px">Tell us about your Party</h1>
    <div class="card">
      <div class="card-h">When is your Party?</div>
      <div class="note" style="font-size:4.3px"><span class="dot">i</span><span>WE WILL PICK UP THE EMPTY KEG THE NEXT DAY</span></div>
      <div class="field">Select Date<svg viewBox="0 0 10 10"><rect x="1" y="2" width="8" height="7" rx="1" fill="none" stroke="#f7931e"/><path d="M1 4.5h8M3 1v2M7 1v2" stroke="#f7931e"/></svg></div>
    </div>
    <div class="card" style="margin-top:13px">
      <div class="card-h">Tell us about the People Attending</div>
      <div class="slider-l">Booze Hound (good for 8 pints)</div>
      <div class="slider"><span class="num">8</span><span class="track"><i style="width:80%"></i><b style="left:77%"></b></span></div>
      <div class="slider-l">Thirsty but Thoughtful (good for 3 pints)</div>
      <div class="slider"><span class="num">4</span><span class="track"><i style="width:46%"></i><b style="left:43%"></b></span></div>
      <div class="slider-l">Country club bore (good for 2 pints)</div>
      <div class="slider"><span class="num">6</span><span class="track"><i style="width:68%"></i><b style="left:65%"></b></span></div>
    </div>
    <div class="card" style="margin-top:13px">
      <div class="card-h">What kind of beer do you like?</div>
      <div class="field">Select Beer<svg viewBox="0 0 10 10"><path d="M3 4l2 2 2-2" fill="none" stroke="#f7931e"/></svg></div>
      <div class="card-h" style="margin-top:14px">What kind of glassware do you require?</div>
      <div class="field">Select Glass<svg viewBox="0 0 10 10"><path d="M3 4l2 2 2-2" fill="none" stroke="#f7931e"/></svg></div>
    </div>
  </div>
  <div class="btn" style="position:absolute;left:14px;right:14px;top:496px">Show Recommendations</div>
  <div class="home-bar"></div>
</section>

<!-- ============ Here is what we Think ============ -->
<section class="screen" style="left:79px;top:965px;height:570px">
  <div class="status"><span>9:41</span><svg viewBox="0 0 30 8"><rect x="0" y="5" width="2" height="3" fill="#1f1f1f"/><rect x="3" y="3.5" width="2" height="4.5" fill="#1f1f1f"/><rect x="6" y="2" width="2" height="6" fill="#1f1f1f"/><path d="M11 3.5a5 5 0 0 1 6 0L14 7z" fill="#1f1f1f"/><rect x="20" y="1.5" width="9" height="5" rx="1.2" fill="#1f1f1f"/></svg></div>
  <div class="pad">
    <div class="hero" style="margin-top:0">
      <div class="back" style="position:absolute;left:8px;top:8px;background:#fff"><svg viewBox="0 0 10 10"><path d="M6.5 2 3.5 5l3 3" fill="none" stroke="#f7931e" stroke-width="1.5"/></svg></div>
      <div class="art art-mugs" role="img" aria-label="Cartoon of clinking beer mugs with an excited emoji"></div>
      <div class="msg">Based on what you told us we think you need at least:</div>
      <div class="pints">72<small>PINTS</small></div>
    </div>
    <h1 class="title" style="font-size:10.5px;margin-top:12px">Here is what we Think</h1>
    <div class="sub">These bundles should make your party awesome</div>
    <div class="prod" style="border-color:#f7d6ae">
      <div class="keg" role="img" aria-label="Blue 35 litre keg of Session IPA">
        <span class="badge">● FEATURED</span>
        <div class="stats"><span>5.2%<small>VOL</small></span><span>4.5<small>★★★★★</small></span></div>
        <div class="spec">2x 35l keg • 40 plastic cups • Simple tap</div>
      </div>
      <div class="brew-row"><span class="brew-dot"></span><span class="nm"><small>TALLOWMERE BREWING</small>Session IPA</span><span class="price-btn">£110.50</span></div>
    </div>
    <div class="prod" style="margin-top:14px">
      <div class="prod-alt">
        <div class="img" role="img" aria-label="Red keg of Ironworks Porter"></div>
        <div>
          <div class="minst"><span>5.2%<small>VOL</small></span><span>4.5<small>★★★★★</small></span></div>
          <div class="bul">• 2x 35l keg<br>• 40 plastic cups<br>• Simple tap</div>
          <div class="pr">£110.50</div>
        </div>
      </div>
      <div class="brew-row"><span class="brew-dot"></span><span class="nm"><small>TALLOWMERE BREWING</small>Ironworks Porter</span><span class="price-btn" style="font-size:5.5px">Choose</span></div>
    </div>
    <div class="prod" style="margin-top:14px">
      <div class="prod-alt">
        <div class="img yel" role="img" aria-label="Yellow keg of pale ale"></div>
        <div>
          <div class="minst"><span>5.2%<small>VOL</small></span><span>4.5<small>★★★★★</small></span></div>
          <div class="bul">• 2x 35l keg</div>
        </div>
      </div>
    </div>
  </div>
</section>

<!-- ============ My Basket ============ -->
<section class="screen" style="left:353px;top:965px;height:614px">
  <div class="status"><span>9:41</span><svg viewBox="0 0 30 8"><rect x="0" y="5" width="2" height="3" fill="#1f1f1f"/><rect x="3" y="3.5" width="2" height="4.5" fill="#1f1f1f"/><rect x="6" y="2" width="2" height="6" fill="#1f1f1f"/><path d="M11 3.5a5 5 0 0 1 6 0L14 7z" fill="#1f1f1f"/><rect x="20" y="1.5" width="9" height="5" rx="1.2" fill="#1f1f1f"/></svg></div>
  <div class="pad" style="margin-top:4px">
    <div class="back"><svg viewBox="0 0 10 10"><path d="M6.5 2 3.5 5l3 3" fill="none" stroke="#fff" stroke-width="1.5"/></svg></div>
    <h1 class="title" style="font-size:11px">My Basket</h1>
    <div class="sub">You have 3 items in your basket</div>
    <div class="item"><div class="img" style="background:linear-gradient(160deg,#e3443a,#8c1d1d)" role="img" aria-label="Red keg of Ironworks Porter"></div>
      <div class="body"><span class="x">×</span><div class="nm">Ironworks Porter</div><div class="sz">35l Keg</div>
        <div class="qty">£110.50<span class="c"><span class="m">−</span>1<span class="p">+</span></span></div></div></div>
    <div class="item"><div class="img" style="background:linear-gradient(160deg,#3a73e0,#1b3f99)" role="img" aria-label="Blue keg of Brookline ale"></div>
      <div class="body"><span class="x">×</span><div class="nm">Brookline</div><div class="sz">20 Keg</div>
        <div class="qty">£110.50<span class="c"><span class="m">−</span>1<span class="p">+</span></span></div></div></div>
    <div class="item"><div class="img" style="background:linear-gradient(160deg,#d08a3c,#5b3a22)" role="img" aria-label="Hand holding a glass of beer"></div>
      <div class="body"><span class="x">×</span><div class="nm">Returnable Glasses</div><div class="sz">&nbsp;</div>
        <div class="qty">£35.00<span class="c"><span class="m">−</span>15<span class="p">+</span></span></div></div></div>
    <div class="subtotal"><span>Sub Total</span><b>£256.00</b></div>
    <div class="sec">Recommended with your Order</div>
    <div class="rec">
      <div class="tile"><div class="img" style="background:linear-gradient(160deg,#6b7a8c,#2f3742)" role="img" aria-label="Kegerator beer cooler"></div>
        <div class="t"><div class="nm">Kegerator</div><div class="ds">Keep your keg chilled throughout</div><div class="row">£35.00<span class="add">+ ADD</span></div></div></div>
      <div class="peek" style="background:#2f3742" role="img" aria-label="Another recommended accessory"></div>
    </div>
    <div class="sec">Something on the Side</div>
    <div class="rec">
      <div class="tile"><div class="img" style="background:linear-gradient(160deg,#e8b060,#8a5a2b)" role="img" aria-label="Bowls of crisps"></div>
        <div class="t"><div class="nm">Crisps Selection</div><div class="ds">3 bags of crisps</div><div class="row">£5.00<span class="add">+ ADD</span></div></div></div>
      <div class="peek" style="background:linear-gradient(160deg,#f2c14e,#d9442b)" role="img" aria-label="Another side snack"></div>
    </div>
  </div>
  <div class="btn" style="position:absolute;left:14px;right:14px;top:548px">Go to Checkout</div>
  <div class="home-bar"></div>
</section>

<!-- ============ Checkout – Delivery Details ============ -->
<section class="screen" style="left:629px;top:965px;height:744px">
  <div class="sheet-top"><div class="status on-orange"><span>9:41</span><svg viewBox="0 0 30 8"><rect x="0" y="5" width="2" height="3" fill="#fff"/><rect x="3" y="3.5" width="2" height="4.5" fill="#fff"/><rect x="6" y="2" width="2" height="6" fill="#fff"/><path d="M11 3.5a5 5 0 0 1 6 0L14 7z" fill="#fff"/><rect x="20" y="1.5" width="9" height="5" rx="1.2" fill="#fff"/></svg></div></div>
  <div class="sheet">
    <div class="co-head"><span class="back-plain"><svg viewBox="0 0 10 10"><path d="M6.5 2 3.5 5l3 3" fill="none" stroke="#f7931e" stroke-width="1.5"/></svg></span><span class="t">Checkout</span></div>
    <svg class="stepper" viewBox="0 0 150 22" aria-hidden="true"><line x1="20" y1="11" x2="130" y2="11" stroke="#f7d6ae" stroke-width="1.5"/><circle cx="20" cy="11" r="10" fill="#fde6c8"/><circle cx="20" cy="11" r="7" fill="#f7931e"/><path d="M20 15s3-3 3-5a3 3 0 0 0-6 0c0 2 3 5 3 5z" fill="#fff"/><circle cx="75" cy="11" r="8" fill="#fff" stroke="#f7d6ae"/><rect x="71.5" y="8" width="7" height="6" rx="1" fill="none" stroke="#f7c48a"/><circle cx="130" cy="11" r="8" fill="#fff" stroke="#f7d6ae"/><rect x="127" y="7.5" width="6" height="7" rx="1" fill="none" stroke="#f7c48a"/></svg>
    <div class="pad">
      <div class="co-title">Delivery Details</div>
      <div class="label">CUSTOMER NAME</div><div class="field grey">Enter name</div>
      <div class="label" style="margin-top:12px">EMAIL ADDRESS</div><div class="field grey">Enter email</div>
      <div class="label" style="margin-top:12px">PHONE NUMBER</div><div class="field grey">Enter contact number</div>
      <div class="label" style="margin-top:12px">DELIVERY DATE</div><div class="field dark">Select Date<svg viewBox="0 0 10 10"><rect x="1" y="2" width="8" height="7" rx="1" fill="none" stroke="#f7931e"/><path d="M1 4.5h8M3 1v2M7 1v2" stroke="#f7931e"/></svg></div>
      <div class="label" style="margin-top:12px">ADDRESS</div><div class="field dark">Accomodation Type<svg viewBox="0 0 10 10"><path d="M3 4l2 2 2-2" fill="none" stroke="#f7931e"/></svg></div>
      <div class="map" role="img" aria-label="Street map with a pin at the delivery address"></div>
      <div class="field dark" style="margin-top:10px">Select State/Province<svg viewBox="0 0 10 10"><path d="M3 4l2 2 2-2" fill="none" stroke="#f7931e"/></svg></div>
      <div class="field dark">Select City<svg viewBox="0 0 10 10"><path d="M3 4l2 2 2-2" fill="none" stroke="#f7931e"/></svg></div>
      <div class="field dark">ZIP Code<svg viewBox="0 0 10 10"><path d="M3 4l2 2 2-2" fill="none" stroke="#f7931e"/></svg></div>
      <div style="font-size:5.5px;margin-top:10px">Detailed Address</div>
      <div class="sub" style="font-size:4.3px;margin-top:2px">Unit number, house number, building, street name</div>
      <div class="field dark" style="font-weight:400">14 Wharf Lane</div>
      <div class="btn-row" style="margin-top:14px"><div class="btn ghost">Back</div><div class="btn">Next</div></div>
    </div>
  </div>
  <div class="home-bar"></div>
</section>

<!-- ============ Checkout – Payment Details ============ -->
<section class="screen" style="left:904px;top:1070px;height:465px">
  <div class="sheet-top"><div class="status on-orange"><span>9:41</span><svg viewBox="0 0 30 8"><rect x="0" y="5" width="2" height="3" fill="#fff"/><rect x="3" y="3.5" width="2" height="4.5" fill="#fff"/><rect x="6" y="2" width="2" height="6" fill="#fff"/><path d="M11 3.5a5 5 0 0 1 6 0L14 7z" fill="#fff"/><rect x="20" y="1.5" width="9" height="5" rx="1.2" fill="#fff"/></svg></div></div>
  <div class="sheet">
    <div class="co-head"><span class="back-plain"><svg viewBox="0 0 10 10"><path d="M6.5 2 3.5 5l3 3" fill="none" stroke="#f7931e" stroke-width="1.5"/></svg></span><span class="t">Checkout</span></div>
    <svg class="stepper" viewBox="0 0 150 22" aria-hidden="true"><line x1="20" y1="11" x2="75" y2="11" stroke="#f7931e" stroke-width="1.5"/><line x1="75" y1="11" x2="130" y2="11" stroke="#f7d6ae" stroke-width="1.5"/><circle cx="20" cy="11" r="8" fill="#f7931e"/><path d="M20 15s3-3 3-5a3 3 0 0 0-6 0c0 2 3 5 3 5z" fill="#fff"/><circle cx="75" cy="11" r="10" fill="#fde6c8"/><circle cx="75" cy="11" r="7" fill="#f7931e"/><rect x="72" y="8.5" width="6" height="5" rx="1" fill="none" stroke="#fff"/><circle cx="130" cy="11" r="8" fill="#fff" stroke="#f7d6ae"/><rect x="127" y="7.5" width="6" height="7" rx="1" fill="none" stroke="#f7c48a"/></svg>
    <div class="pad">
      <div class="co-title">Payment Details</div>
      <div class="card">
        <div class="card-h" style="font-size:5.5px">Select Payment Method</div>
        <div class="pay-opts">
          <div class="pay-opt"><span class="sq"></span>Vexa Pay</div>
          <div class="pay-opt"><span class="sq" style="background:#1f3c88"></span>Brightpay</div>
          <div class="pay-opt sel"><span class="sq"></span>Card</div>
        </div>
        <div style="font-size:5.5px;text-align:center;margin-top:12px">Credit Card Details (Quillpay)</div>
        <div class="ccard">
          <div class="card-band" role="img" aria-label="Decorative beer foam band"></div>
          <span class="num">2048  60XX  XXXX  0279</span>
          <span class="holder">Maren Holt</span>
          <span class="qp">quillpay</span>
          <span class="net">Carda</span>
        </div>
      </div>
      <div class="agree"><span class="box"><svg viewBox="0 0 10 10" width="6" height="6"><path d="M2 5l2 2 4-4" fill="none" stroke="#fff" stroke-width="1.6"/></svg></span>I agree to the <a>Terms &amp; Conditions</a> and <a>Privacy Policy</a></div>
      <div class="btn-row" style="margin-top:26px"><div class="btn ghost">Back</div><div class="btn">Next</div></div>
    </div>
  </div>
  <div class="home-bar"></div>
</section>

<!-- ============ Checkout – Place Order ============ -->
<section class="screen" style="left:79px;top:1595px;height:465px">
  <div class="sheet-top"><div class="status on-orange"><span>9:41</span><svg viewBox="0 0 30 8"><rect x="0" y="5" width="2" height="3" fill="#fff"/><rect x="3" y="3.5" width="2" height="4.5" fill="#fff"/><rect x="6" y="2" width="2" height="6" fill="#fff"/><path d="M11 3.5a5 5 0 0 1 6 0L14 7z" fill="#fff"/><rect x="20" y="1.5" width="9" height="5" rx="1.2" fill="#fff"/></svg></div></div>
  <div class="sheet">
    <div class="co-head"><span class="back-plain"><svg viewBox="0 0 10 10"><path d="M6.5 2 3.5 5l3 3" fill="none" stroke="#f7931e" stroke-width="1.5"/></svg></span><span class="t">Checkout</span></div>
    <svg class="stepper" viewBox="0 0 150 22" aria-hidden="true"><line x1="20" y1="11" x2="130" y2="11" stroke="#f7931e" stroke-width="1.5"/><circle cx="20" cy="11" r="8" fill="#f7931e"/><path d="M20 15s3-3 3-5a3 3 0 0 0-6 0c0 2 3 5 3 5z" fill="#fff"/><circle cx="75" cy="11" r="8" fill="#f7931e"/><rect x="72" y="8.5" width="6" height="5" rx="1" fill="none" stroke="#fff"/><circle cx="130" cy="11" r="10" fill="#fde6c8"/><circle cx="130" cy="11" r="7" fill="#f7931e"/><rect x="127.5" y="8" width="5" height="6" rx="1" fill="none" stroke="#fff"/></svg>
    <div class="pad">
      <div class="co-title">Place Order</div>
      <div class="receipt"><div class="paper">
        <div class="rline">My Basket Sub-Total<b>£256.00</b></div>
        <div class="rline">Delivery Fee<b>£3.00</b></div>
        <div class="rline" style="margin-bottom:26px">Tip (10% of 256.00)<b>$2.56</b></div>
        <div class="rline total">Grand Total<b>$11.51</b></div>
      </div></div>
      <div class="toggle-row" style="margin-top:20px">Stay Updated on News and Special Offers<span class="tog"></span></div>
      <div class="toggle-row">Share Info with our Brewer Partners<span class="tog on"></span></div>
    </div>
  </div>
  <div class="btn" style="position:absolute;left:14px;right:14px;top:400px">PLACE ORDER NOW</div>
  <div class="home-bar"></div>
</section>

<!-- ============ Order Placed ============ -->
<section class="screen" style="left:353px;top:1640px;height:465px">
  <div class="status"><span>9:41</span><svg viewBox="0 0 30 8"><rect x="0" y="5" width="2" height="3" fill="#1f1f1f"/><rect x="3" y="3.5" width="2" height="4.5" fill="#1f1f1f"/><rect x="6" y="2" width="2" height="6" fill="#1f1f1f"/><path d="M11 3.5a5 5 0 0 1 6 0L14 7z" fill="#1f1f1f"/><rect x="20" y="1.5" width="9" height="5" rx="1.2" fill="#1f1f1f"/></svg></div>
  <div class="pad success">
    <div style="text-align:left;margin-top:6px"><svg viewBox="0 0 10 10" width="9" height="9"><path d="M2 2l6 6M8 2 2 8" stroke="#f7931e" stroke-width="1.3"/></svg></div>
    <div class="ring">
      <div class="art" role="img" aria-label="Cartoon of two clinking beer mugs"></div>
      <span class="tick"><svg viewBox="0 0 10 10" width="8" height="8"><path d="M2 5l2 2 4-4" fill="none" stroke="#fff" stroke-width="1.6"/></svg></span>
    </div>
    <h2>Order Placed Successfully!</h2>
    <p>We have received your order.<br>Get ready to party!</p>
    <p>An order confirmation email will be sent to<br><b>party.maren@email.com</b></p>
    <div class="divider">You bought beer from</div>
    <div class="brew-mark"><span class="circ"></span>Tallowmere Brewing</div>
    <span class="learn">LEARN MORE</span>
  </div>
  <div class="btn" style="position:absolute;left:18px;right:18px;top:400px">Buy More</div>
  <div class="home-bar"></div>
</section>

</body>
</html>
```